Website for software company "velbra"

We need a website for our software company/startup named "velbra". We are developing several products (currently 3 standard-software products) which are all in different sectors, but all our products are available for Laptops/PC/Mobile Phones/Tablets, ... We do also create custom software and support our customers with consulting to optimize their processes.
We already have a Logo which you can find in the attached files.
We are a young team of 4 members (two founders and 2 employees).

To get an idea of our products -> the first one is a planning software for healthcare organizations (eg. Mercyway, firebrigade, pharmacy), the second one is a booking software for sport clubs and the third one is a competition software for sports hunting. You see very diverse. Include or ignore this info of our products as you like.

The design has to be a bootstrap 4 (or higher) design. We have licenced FontAwesome as iconset. Responsive design should come without saying.

Coding

Coded - Design and coding required

Number of Pages Required

5+ page

Font styles to use
Sans Serif

Requirements
Must have
• Starting page, product pages, news section, contact, team, services

```html
<!DOCTYPE html>
<html lang="en">
<head>
<meta charset="utf-8">
<title>velbra — Software Development Company</title>
<link rel="stylesheet" href="https://fonts.googleapis.com/css2?family=Montserrat:wght@400;500;600;700&family=Open+Sans:ital,wght@0,400;0,600;0,700;1,400;1,600&display=swap">
<style>
:root{
  --orange:#f07a23;
  --orange-soft:#f39a57;
  --navy:#1c2738;
  --ink:#2b2f36;
  --text:#3a3f47;
  --muted:#8a9099;
  --panel:#eef0f3;
  --dark-box:#2c3139;
  --white:#ffffff;
  --line:#e2e5ea;
}
*{box-sizing:border-box;margin:0;padding:0}
html,body{width:1200px;height:5204px;overflow:hidden;background:var(--white)}
body{font-family:"Open Sans",Arial,sans-serif;color:var(--text)}
.page{position:relative;width:1200px;height:5204px;overflow:hidden}
.abs{position:absolute}
.heading{font-family:"Montserrat",Arial,sans-serif;font-weight:500;color:var(--ink)}
.btn{position:absolute;background:var(--orange);color:var(--white);font:700 11px "Open Sans",sans-serif;text-transform:uppercase;letter-spacing:.3px;display:flex;align-items:center;justify-content:center}
.eyebrow{position:absolute;font:700 10px "Open Sans",sans-serif;letter-spacing:2px;text-transform:uppercase;color:var(--ink);display:flex;align-items:center;gap:14px}
.eyebrow.center{left:0;width:1200px;justify-content:center}
.dash{display:inline-block;width:76px;height:2px;background:var(--orange);position:relative}
.dash::after{content:"";position:absolute;top:-4px;width:6px;height:6px;border:2px solid var(--orange);border-radius:50%;background:var(--white)}
.dash.end::after{right:-8px}
.dash.start::after{left:-8px}
.section-title{position:absolute;left:0;width:1200px;text-align:center;font-size:34px}

/* hero */
.hero{position:absolute;left:0;top:0;width:1200px;height:717px;background:linear-gradient(100deg,#142033 0%,#1c2a40 40%,#3a4a5e 62%,#7b7f88 80%,#5b6a7c 100%)}
.hero-photo{position:absolute;left:560px;top:70px;width:640px;height:647px;background:radial-gradient(ellipse at 40% 40%,rgba(230,196,160,.45),rgba(120,130,140,.25) 55%,rgba(28,39,56,0) 80%)}
.topbar-email{position:absolute;left:634px;top:0;height:36px;display:flex;align-items:center;gap:8px;color:var(--white);font-size:11px}
.topbar-call{position:absolute;left:852px;top:0;width:220px;height:36px;background:var(--orange);clip-path:polygon(0 0,100% 0,92% 100%,8% 100%);color:var(--white);font-size:11px;font-weight:700;display:flex;align-items:center;justify-content:center;gap:8px}
.brand{position:absolute;font:700 44px "Montserrat",sans-serif;letter-spacing:1px;color:var(--white);line-height:1;display:flex;align-items:center;gap:10px}
.brand .mark{width:14px;height:14px;background:var(--orange)}
.nav{position:absolute;left:650px;top:72px;display:flex;gap:52px;font-size:12px;color:var(--white);letter-spacing:.5px}
.hero-kicker{position:absolute;left:120px;top:228px;font:italic 600 15px "Open Sans",sans-serif;color:var(--white);display:flex;align-items:center;gap:6px}
.kicker-lines{position:relative;width:130px;height:12px}
.kicker-lines i{position:absolute;left:0;height:2px;background:var(--orange)}
.hero-title{position:absolute;left:118px;top:256px;font:500 60px/61px "Montserrat",sans-serif;color:var(--white)}
.hero-lead{position:absolute;left:120px;top:450px;width:440px;font-size:19px;line-height:31px;color:var(--white)}
.slider-rail{position:absolute;left:818px;top:714px;width:382px;height:3px;background:var(--orange)}
.slider-dot{position:absolute;width:30px;height:30px;border-radius:50%;background:var(--orange);border:6px solid var(--white);box-shadow:0 0 0 1px var(--orange)}

/* about */
.about-art{position:absolute;left:121px;top:875px;width:392px;height:300px;background:linear-gradient(120deg,#e9a36c,#d9844a 45%,#f0b888 70%,#cf7a3c)}
.about-title{position:absolute;left:622px;top:868px;font-size:34px}
.about-lead{position:absolute;left:622px;top:952px;width:410px;font-size:13.5px;line-height:26px;color:var(--text)}
.about-body{position:absolute;left:622px;top:1016px;width:410px;font-size:12.5px;line-height:25px;color:var(--muted)}

/* services */
.services{position:absolute;left:0;top:1327px;width:1200px;height:1028px;background:var(--panel)}
.services-photo{position:absolute;left:0;top:1990px;width:1200px;height:365px;background:linear-gradient(180deg,#c9b9a5 0%,#a2765a 45%,#5a3f32 80%,#3c6f78 100%)}
.service-card{position:absolute;width:331px;height:246px;background:var(--white);padding:7px;box-shadow:0 4px 14px rgba(0,0,0,.12)}
.service-card .shot{width:100%;height:100%;position:relative;display:flex;align-items:flex-end;justify-content:center;padding-bottom:22px;color:var(--white);font-size:14px;font-weight:600}
.shot.a{background:linear-gradient(180deg,#d7dde3,#8d97a3 60%,#3d4652)}
.shot.b{background:linear-gradient(180deg,#5b6e80,#2d3b4b 60%,#1a2431)}
.shot.c{background:linear-gradient(180deg,#7d8b97,#43505d 60%,#262f39)}
.shot.d{background:linear-gradient(180deg,#9fb8d1,#3b5c88 55%,#1c2c4c)}
.shot.e{background:linear-gradient(180deg,#4b5664,#232b36 60%,#151b23)}
.shot.f{background:linear-gradient(180deg,#b9c0c7,#6a747e 60%,#353d46)}

/* expertise */
.sector{position:absolute;width:176px;text-align:center;top:2567px}
.sector .ring{width:93px;height:93px;border-radius:50%;background:#fde6d6;margin:0 auto;display:flex;align-items:center;justify-content:center}
.sector .label{margin-top:23px;font-size:12.5px;color:var(--ink)}
.chev{position:absolute;top:2600px;width:20px;height:28px}
.progress{position:absolute;left:0;top:2802px;width:378px;height:3px;background:var(--orange)}

/* tech */
.tech{position:absolute;left:0;top:2808px;width:1200px;height:481px;background:var(--panel)}
.tech-grid{position:absolute;left:123px;top:3014px;width:952px;height:190px;display:grid;grid-template-columns:repeat(5,1fr);grid-template-rows:repeat(2,1fr);gap:4px}
.tech-grid div{background:var(--white);display:flex;align-items:center;justify-content:center;font:600 22px "Montserrat",sans-serif;color:#b5bac1}

/* team */
.member{position:absolute;top:3450px;width:221px;height:334px}
.member .photo{width:100%;height:100%;background:linear-gradient(180deg,#9aa3ad,#c9d2db 55%,#8796a6)}
.member .name{position:absolute;left:0;right:0;bottom:16px;text-align:center;color:var(--white);font:500 22px "Montserrat",sans-serif}
.member .corner{position:absolute;width:22px;height:22px;border-color:var(--orange);border-style:solid}
.member .corner.bl{left:6px;bottom:6px;border-width:0 0 3px 3px}
.member .corner.br{right:6px;bottom:6px;border-width:0 3px 3px 0}

/* testimonial */
.testimonials{position:absolute;left:0;top:3862px;width:1200px;height:515px;background:var(--panel)}
.testi-photo{position:absolute;left:127px;top:3935px;width:301px;height:360px;background:linear-gradient(180deg,#8d959e,#cfd5dc 60%,#aab2bb)}
.testi-box{position:absolute;left:388px;top:4068px;width:672px;height:231px;background:var(--dark-box)}
.quote-mark{position:absolute;left:52px;top:30px;font:700 56px Georgia,serif;color:#6a707a;line-height:1}
.quote-text{position:absolute;left:56px;top:62px;width:580px;color:#e9ebee;font:400 15px/26px "Montserrat",sans-serif}
.stars{position:absolute;left:0;width:100%;top:150px;text-align:center;color:var(--orange);font-size:20px;letter-spacing:3px}
.round-btn{position:absolute;top:3989px;width:38px;height:38px;border-radius:50%;background:var(--dark-box);display:flex;align-items:center;justify-content:center}

/* contact */
.contact{position:absolute;left:0;top:4377px;width:1200px;height:475px;background:var(--orange)}
.contact .eyebrow{color:var(--white)}
.contact .dash{background:var(--white)}
.contact .dash::after{border-color:var(--white);background:var(--orange)}
.field{position:absolute;border:1px solid rgba(255,255,255,.55);background:rgba(255,255,255,.12);color:rgba(255,255,255,.9);font-size:10.5px;padding:12px 18px}
.submit{position:absolute;left:614px;top:4725px;width:144px;height:44px;border:2px solid var(--white);color:var(--white);font-weight:700;font-size:11px;display:flex;align-items:center;justify-content:center}

/* footer */
.footer-brand{position:absolute;left:212px;top:4975px;font:700 44px "Montserrat",sans-serif;color:var(--ink);display:flex;align-items:center;gap:10px;line-height:1}
.footer-brand .mark{width:14px;height:14px;background:var(--orange)}
.social{position:absolute;top:5039px;width:28px;height:28px;border:2px solid var(--orange);border-radius:50%}
.social::after{content:"";position:absolute;left:9px;top:9px;width:6px;height:6px;border-radius:50%;background:var(--orange)}
.foot-head{position:absolute;top:4926px;font:600 15px "Montserrat",sans-serif;color:var(--ink)}
.foot-link{position:absolute;left:561px;font-size:11px;color:var(--muted)}
.foot-info{position:absolute;left:818px;font-size:11px;line-height:22px;color:var(--muted)}
.copyright{position:absolute;left:0;width:1200px;top:5146px;text-align:center;font-size:9.5px;color:var(--text)}
</style>
</head>
<body>
<div class="page">

  <!-- Hero -->
  <header class="hero">
    <div class="hero-photo" role="img" aria-label="Photo of a smiling young woman working on a laptop in an office"></div>
  </header>
  <div class="topbar-email">
    <svg width="14" height="10" viewBox="0 0 14 10"><rect x="0.7" y="0.7" width="12.6" height="8.6" fill="none" stroke="#fff" stroke-width="1.2"/><path d="M1 1l6 5 6-5" fill="none" stroke="#fff" stroke-width="1.2"/></svg>
    EMAIL: info@velbra.com
  </div>
  <div class="topbar-call">
    <svg width="13" height="13" viewBox="0 0 24 24"><path d="M6.6 10.8a15 15 0 006.6 6.6l2.2-2.2c.3-.3.7-.4 1-.2 1.1.4 2.3.6 3.6.6.6 0 1 .4 1 1V20c0 .6-.4 1-1 1A17 17 0 013 4c0-.6.4-1 1-1h3.5c.6 0 1 .4 1 1 0 1.3.2 2.5.6 3.6.1.3 0 .7-.2 1z" fill="#fff"/></svg>
    CALL US: 123.456.7890
  </div>
  <div class="brand" style="left:121px;top:70px"><span class="mark"></span>velbra</div>
  <nav class="nav"><span>HOME</span><span>PRODUCT</span><span>NEWS</span><span>CONTACT</span><span>TEAM</span></nav>
  <div class="hero-kicker">Business And Technology
    <span class="kicker-lines"><i style="top:2px;width:124px"></i><i style="top:9px;width:110px"></i></span>
  </div>
  <h1 class="hero-title">Software<br>Development<br>Company</h1>
  <p class="hero-lead">Lorem ipsum dolor sit amet, consectetuer adipiscing elit.</p>
  <div class="btn" style="left:119px;top:527px;width:194px;height:45px">Contact us today</div>
  <div class="slider-rail"></div>
  <div class="slider-dot" style="left:803px;top:700px"></div>

  <!-- About -->
  <div class="about-art" role="img" aria-label="Orange-toned collage of team members working together"></div>
  <div class="eyebrow" style="left:622px;top:852px">Who we do <span class="dash end"></span></div>
  <h2 class="heading about-title">About Us</h2>
  <p class="about-lead">Lorem ipsum dolor sit amet, consectetuer adipiscing elit, sed diam nonummy nibh euismod tincidunt ut .</p>
  <p class="about-body">Ut wisi enim ad minim veniam, quis nostrud exerci tation suscipit lobortis nisl ut aliquip ex ea commodo consequat. Duis autem vel eum iriure dolor in hendrerit in velit esse molestie consequatvel illum dolore eu</p>
  <div class="btn" style="left:622px;top:1149px;width:194px;height:43px">Contact us today</div>

  <!-- Services -->
  <section class="services"></section>
  <div class="services-photo" role="img" aria-label="Overhead photo of a team collaborating around laptops on a wooden desk"></div>
  <div class="eyebrow center" style="top:1403px"><span class="dash start"></span>What we do<span class="dash end"></span></div>
  <h2 class="heading section-title" style="top:1438px">Services</h2>

  <div class="service-card" style="left:73px;top:1515px"><div class="shot a" role="img" aria-label="Photo of colleagues consulting in a bright office">Software Consulting</div></div>
  <div class="service-card" style="left:432px;top:1515px"><div class="shot b" role="img" aria-label="Photo of hands using a digital interface">Software Development Outsourcing</div></div>
  <div class="service-card" style="left:792px;top:1515px"><div class="shot c" role="img" aria-label="Photo of engineers discussing at a workstation">Team Augmentation</div></div>
  <div class="service-card" style="left:73px;top:1794px"><div class="shot d" role="img" aria-label="Illustration of a cloud over data servers">Legacy Software Modernization</div></div>
  <div class="service-card" style="left:432px;top:1794px"><div class="shot e" role="img" aria-label="Photo of code on a computer screen">Custom Software Development</div></div>
  <div class="service-card" style="left:792px;top:1794px"><div class="shot f" role="img" aria-label="Photo of a product design on a monitor in a studio">Software Product Development</div></div>
  <div class="btn" style="left:509px;top:2080px;width:178px;height:41px">View all services</div>

  <!-- Expertise -->
  <div class="eyebrow center" style="top:2429px"><span class="dash start"></span>Expertise in<span class="dash end"></span></div>
  <h2 class="heading section-title" style="top:2464px">Delivering The Right Solution</h2>
  <svg class="chev" style="left:62px" viewBox="0 0 20 28"><path d="M14 4L5 14l9 10" fill="none" stroke="#2b2f36" stroke-width="2"/></svg>
  <svg class="chev" style="left:1116px" viewBox="0 0 20 28"><path d="M6 4l9 10-9 10" fill="none" stroke="#2b2f36" stroke-width="2"/></svg>

  <div class="sector" style="left:72px"><div class="ring"><svg width="46" height="40" viewBox="0 0 46 40"><rect x="3" y="3" width="40" height="26" fill="none" stroke="#f07a23" stroke-width="2.5"/><path d="M12 11h4l3 9h12l3-7H17" fill="none" stroke="#f07a23" stroke-width="2"/><path d="M15 36h16" stroke="#f07a23" stroke-width="2.5"/></svg></div><div class="label">Retail, Ecommerce</div></div>
  <div class="sector" style="left:247px"><div class="ring"><svg width="44" height="40" viewBox="0 0 44 40"><path d="M22 36S4 25 4 13a9 9 0 0118-3 9 9 0 0118 3c0 12-18 23-18 23z" fill="none" stroke="#f07a23" stroke-width="2.5"/><path d="M28 26l4 4" stroke="#f07a23" stroke-width="2"/></svg></div><div class="label">Healthcare</div></div>
  <div class="sector" style="left:423px"><div class="ring"><svg width="46" height="44" viewBox="0 0 46 44"><rect x="16" y="12" width="14" height="24" rx="2" fill="none" stroke="#f07a23" stroke-width="2.2"/><circle cx="8" cy="22" r="4" fill="none" stroke="#f07a23" stroke-width="2"/><circle cx="38" cy="22" r="4" fill="none" stroke="#f07a23" stroke-width="2"/><circle cx="23" cy="5" r="3.5" fill="none" stroke="#f07a23" stroke-width="2"/></svg></div><div class="label">Social Networking</div></div>
  <div class="sector" style="left:599px"><div class="ring"><svg width="46" height="42" viewBox="0 0 46 42"><path d="M4 20L22 6l18 14" fill="none" stroke="#f07a23" stroke-width="2.5"/><path d="M9 17v20h26V17" fill="none" stroke="#f07a23" stroke-width="2.2"/><rect x="19" y="25" width="8" height="12" fill="none" stroke="#f07a23" stroke-width="2"/></svg></div><div class="label">Real Estate</div></div>
  <div class="sector" style="left:775px"><div class="ring"><svg width="46" height="42" viewBox="0 0 46 42"><path d="M6 18h34v20H6z" fill="none" stroke="#f07a23" stroke-width="2.2"/><path d="M6 18l4-8h26l4 8" fill="none" stroke="#f07a23" stroke-width="2.2"/><rect x="18" y="26" width="10" height="12" fill="none" stroke="#f07a23" stroke-width="2"/></svg></div><div class="label">Food &amp; Restaurant</div></div>
  <div class="sector" style="left:950px"><div class="ring"><svg width="46" height="40" viewBox="0 0 46 40"><rect x="4" y="12" width="38" height="22" rx="3" fill="none" stroke="#f07a23" stroke-width="2.4"/><path d="M13 19v8M9 23h8" stroke="#f07a23" stroke-width="2"/><circle cx="31" cy="21" r="2" fill="#f07a23"/><circle cx="36" cy="26" r="2" fill="#f07a23"/><path d="M23 12V5" stroke="#f07a23" stroke-width="2"/></svg></div><div class="label">Gaming</div></div>

  <div class="progress"></div>
  <div class="slider-dot" style="left:364px;top:2789px"></div>

  <!-- Technology -->
  <section class="tech"></section>
  <div class="eyebrow center" style="top:2882px"><span class="dash start"></span>Advanced<span class="dash end"></span></div>
  <h2 class="heading section-title" style="top:2917px">Technology Stack</h2>
  <div class="tech-grid">
    <div>Serpa</div><div>Gridly</div><div>Corva</div><div>Lumo</div><div>Tesso</div>
    <div>Vanta</div><div>Orbix</div><div>Wisp</div><div>Robix</div><div>Calyx</div>
  </div>

  <!-- Team -->
  <h2 class="heading section-title" style="top:3358px;display:flex;justify-content:center;align-items:center;gap:16px"><span class="dash start"></span>Our Team<span class="dash end"></span></h2>
  <div class="member" style="left:135px"><div class="photo" role="img" aria-label="Portrait photo of a team member"></div><span class="corner bl"></span><span class="corner br"></span><div class="name">Mara Lund</div></div>
  <div class="member" style="left:372px"><div class="photo" role="img" aria-label="Portrait photo of a team member"></div><span class="corner bl"></span><span class="corner br"></span><div class="name">Jonas Pike</div></div>
  <div class="member" style="left:608px"><div class="photo" role="img" aria-label="Portrait photo of a team member"></div><span class="corner bl"></span><span class="corner br"></span><div class="name">Theo Brandt</div></div>
  <div class="member" style="left:846px"><div class="photo" role="img" aria-label="Portrait photo of a team member"></div><span class="corner bl"></span><span class="corner br"></span><div class="name">Evan Holt</div></div>

  <!-- Testimonial -->
  <section class="testimonials"></section>
  <div class="testi-photo" role="img" aria-label="Portrait photo of a client"></div>
  <h2 class="heading" style="position:absolute;left:490px;top:3990px;font-size:30px;display:flex;align-items:center;gap:16px"><span class="dash start"></span>Testimonial<span class="dash end"></span></h2>
  <div class="round-btn" style="left:973px"><svg width="16" height="12" viewBox="0 0 16 12"><path d="M15 6H2M6 1L1 6l5 5" fill="none" stroke="#fff" stroke-width="1.6"/></svg></div>
  <div class="round-btn" style="left:1019px"><svg width="16" height="12" viewBox="0 0 16 12"><path d="M1 6h13M10 1l5 5-5 5" fill="none" stroke="#fff" stroke-width="1.6"/></svg></div>
  <div class="testi-box">
    <div class="quote-mark">&ldquo;</div>
    <p class="quote-text">&nbsp;&nbsp;&nbsp;&nbsp;&nbsp;Dolore magna aliquam erat volutpat. Ut wisi enim ad minim veniam, qu nostrud exerci tation ullamcorper suscipit lobortis nisl ut</p>
    <div class="stars">★★★★★</div>
  </div>

  <!-- Contact -->
  <section class="contact"></section>
  <p style="position:absolute;left:614px;top:4443px;font-style:italic;font-size:13px;color:rgba(255,255,255,.9)">Drop us a line! We are here to answer your questions 24/7.</p>
  <div class="eyebrow" style="left:127px;top:4514px">Get in touch <span class="dash end"></span></div>
  <h2 class="heading" style="position:absolute;left:127px;top:4552px;font-size:30px;color:#fff">Call Us Today</h2>
  <p style="position:absolute;left:127px;top:4609px;font-size:15px;color:#fff">Ready to build your custom software ?</p>
  <div style="position:absolute;left:123px;top:4652px;width:44px;height:44px;border-radius:50%;background:#fff;display:flex;align-items:center;justify-content:center"><svg width="20" height="20" viewBox="0 0 24 24"><path d="M6.6 10.8a15 15 0 006.6 6.6l2.2-2.2c.3-.3.7-.4 1-.2 1.1.4 2.3.6 3.6.6.6 0 1 .4 1 1V20c0 .6-.4 1-1 1A17 17 0 013 4c0-.6.4-1 1-1h3.5c.6 0 1 .4 1 1 0 1.3.2 2.5.6 3.6.1.3 0 .7-.2 1z" fill="#f07a23"/></svg></div>
  <p style="position:absolute;left:185px;top:4664px;font-size:16px;color:#fff">123.456.7890</p>
  <div class="field" style="left:614px;top:4494px;width:225px;height:43px">Full Name</div>
  <div class="field" style="left:872px;top:4494px;width:206px;height:43px">Company Name</div>
  <div class="field" style="left:614px;top:4553px;width:225px;height:44px">Work Email</div>
  <div class="field" style="left:872px;top:4553px;width:206px;height:44px">Work phone</div>
  <div class="field" style="left:614px;top:4612px;width:464px;height:97px">How Can We Help You?</div>
  <div class="submit">SUBMIT</div>
  <div style="position:absolute;left:1004px;top:4850px;width:196px;height:3px;background:#fff"></div>
  <div class="slider-dot" style="left:989px;top:4837px;background:var(--orange)"></div>

  <!-- Footer -->
  <div class="footer-brand"><span class="mark"></span>velbra</div>
  <span class="social" style="left:261px"></span>
  <span class="social" style="left:297px"></span>
  <span class="social" style="left:333px"></span>
  <div class="foot-head" style="left:551px">Quick Link</div>
  <span class="foot-link" style="top:4972px">Home</span>
  <span class="foot-link" style="top:4999px">Product</span>
  <span class="foot-link" style="top:5026px">News</span>
  <span class="foot-link" style="top:5053px">Contact</span>
  <span class="foot-link" style="top:5080px">Team</span>
  <div class="foot-head" style="left:782px">Contact Info</div>
  <svg style="position:absolute;left:780px;top:4975px" width="16" height="22" viewBox="0 0 16 22"><path d="M8 21S2 13 2 8a6 6 0 0112 0c0 5-6 13-6 13z" fill="none" stroke="#f07a23" stroke-width="1.8"/><circle cx="8" cy="8" r="2.2" fill="none" stroke="#f07a23" stroke-width="1.6"/></svg>
  <p class="foot-info" style="top:4966px">Address Lorem ipsum 2360<br>3rd Street Location, AB 91407</p>
  <svg style="position:absolute;left:781px;top:5036px" width="16" height="16" viewBox="0 0 24 24"><path d="M6.6 10.8a15 15 0 006.6 6.6l2.2-2.2c.3-.3.7-.4 1-.2 1.1.4 2.3.6 3.6.6.6 0 1 .4 1 1V20c0 .6-.4 1-1 1A17 17 0 013 4c0-.6.4-1 1-1h3.5c.6 0 1 .4 1 1 0 1.3.2 2.5.6 3.6.1.3 0 .7-.2 1z" fill="none" stroke="#f07a23" stroke-width="2"/></svg>
  <p class="foot-info" style="top:5033px">123.456.7890</p>
  <svg style="position:absolute;left:781px;top:5080px" width="16" height="12" viewBox="0 0 16 12"><rect x="1" y="1" width="14" height="10" fill="none" stroke="#f07a23" stroke-width="1.6"/><path d="M1 1l7 6 7-6" fill="none" stroke="#f07a23" stroke-width="1.6"/></svg>
  <p class="foot-info" style="top:5075px">info@velbra.com</p>
  <p class="copyright">© 2022 velbra. All right reserved</p>

</div>
</body>
</html>
```